Fence Flyer to Attract More Sales During Winter

We need a new flyer made that we can distribute to residential mailboxes. The flyer is to promote our Frostline Picket Days. We like simply designs, and we would like the flyer to showcase a lot of our fence photos. More of our photos are online at our website at www.getbramblerail.com - our new address needs to also be featured on the flyer - 436 Quillen rd, Monroe, NC 28117. I do want the words "FROSTLINE PICKET DAYS" to be dominate on the flyer with the description "Wood fences starting at $12/FT!" Please look through our Facebook page and our website to gather more photos or information. We are flexible on colors, nothing to fancy - simple flyer design please.

Target Market(s)

Residential homeowners that need a new fence to enclose their yard for safety, security or decorative

Industry/Entity Type

Residential Construction

Font styles to use
Sans Serif

Colors

Designer to choose colors to be used in the design.

Requirements
Must have
• Frostline Picket Days
• Contact information for the business
• "Come visit our outdoor showroom, open 24/7!"
Nice to have
• Photos of our fences - you can find more on our website at www.GetBrambleRail.com or Facebook.com/MeadowlarkRailGPV
Should not have
• Flashy designs

```html
<!DOCTYPE html>
<html lang="en">
<head>
<meta charset="utf-8">
<title>Frostline Picket Days – Bramble Rail Fence</title>
<link href="https://fonts.googleapis.com/css2?family=Nunito+Sans:wght@400;600;700;800&display=swap" rel="stylesheet">
<style>
  :root {
    --blue: #3a83c9;
    --ink: #2a211b;
    --band: #e4e6e6;
    --brown: #553d2b;
    --white: #ffffff;
    --accent: #f0932b;
  }
  * { margin: 0; padding: 0; box-sizing: border-box; }
  html, body { width: 873px; height: 1200px; overflow: hidden; background: var(--white); }
  body { font-family: "Nunito Sans", sans-serif; }
  .flyer { position: relative; width: 873px; height: 1200px; overflow: hidden; background: var(--white); }

  .brand { position: absolute; left: 54px; top: 36px; display: flex; align-items: flex-start; gap: 14px; }
  .brand-dot { width: 22px; height: 22px; border-radius: 50%; background: var(--accent); margin-top: 8px; }
  .brand-name { font-size: 27px; font-weight: 800; color: var(--blue); line-height: 32px; }
  .brand-phone { font-size: 26px; font-weight: 800; color: var(--ink); line-height: 32px; }
  .brand-tagline { font-size: 9px; font-weight: 700; color: var(--ink); margin-top: 6px; }

  .promo-band { position: absolute; left: 0; top: 198px; width: 873px; height: 432px; background: var(--band); }

  .headline { position: absolute; left: 52px; top: 212px; width: 440px; color: var(--blue); font-weight: 700;
    font-size: 68px; line-height: 95px; letter-spacing: 2px; white-space: nowrap; }
  .offer { position: absolute; left: 54px; top: 530px; color: var(--blue); font-weight: 700;
    font-size: 34px; line-height: 38px; letter-spacing: 0.5px; white-space: nowrap; }

  .photo { position: absolute; }
  .photo-rounded { border-radius: 42px 0 42px 0; }
  .photo-gate-wire { left: 508px; top: 170px; width: 315px; height: 327px;
    background: linear-gradient(180deg, #4d5a3a 0%, #7d8b55 35%, #d9c08a 55%, #b98f62 100%); }
  .photo-gate-yard { left: 508px; top: 534px; width: 315px; height: 327px;
    background: linear-gradient(180deg, #3f6a2e 0%, #7fae4c 38%, #d6b887 62%, #8a6a48 100%); }
  .photo-privacy { left: 53px; top: 681px; width: 174px; height: 180px; border-radius: 30px 0 30px 0;
    background: linear-gradient(180deg, #8aa2bf 0%, #b7765a 30%, #e8d29f 55%, #a58a6a 100%); }
  .photo-split-rail { left: 278px; top: 681px; width: 174px; height: 180px; border-radius: 30px 0 30px 0;
    background: linear-gradient(180deg, #2e4d22 0%, #5f7d3d 40%, #c9ad7b 65%, #8b7050 100%); }

  .footer { position: absolute; left: 0; top: 898px; width: 873px; height: 302px; background: var(--brown); color: var(--white); }
  .contact-row { position: absolute; display: flex; align-items: center; white-space: nowrap; font-size: 17px; }
  .contact-icon { width: 34px; height: 34px; flex: none; }
  .social-dot { width: 34px; height: 34px; border-radius: 50%; background: var(--blue); flex: none; }
  .divider-v { position: absolute; left: 373px; top: 26px; width: 3px; height: 204px; background: var(--blue); }
  .hours { position: absolute; left: 392px; top: 34px; font-size: 17px; line-height: 23.4px; white-space: nowrap; }
  .divider-h { position: absolute; left: 50px; top: 243px; width: 773px; height: 3px; background: var(--blue); }
  .showroom { position: absolute; left: 0; top: 252px; width: 873px; text-align: center; font-size: 28px; line-height: 40px; }
</style>
</head>
<body>
<div class="flyer">
  <header class="brand">
    <span class="brand-dot"></span>
    <div>
      <div class="brand-name">Bramble Rail Fence</div>
      <div class="brand-phone">704-555-0147</div>
      <div class="brand-tagline">"Because Good Fences Make Good Neighbors"</div>
    </div>
  </header>

  <div class="promo-band"></div>
  <h1 class="headline">FROSTLINE<br>PICKET<br>DAYS</h1>
  <p class="offer">WOOD FENCES<br>STARTING AT $12/FT!</p>

  <div class="photo photo-rounded photo-gate-wire" role="img" aria-label="Photo of an arched wood gate set in a wire-panel rail fence among trees"></div>
  <div class="photo photo-rounded photo-gate-yard" role="img" aria-label="Photo of a curved-top wood picket fence section beside a green lawn"></div>
  <div class="photo photo-privacy" role="img" aria-label="Photo of a new wood picket privacy fence in front of a brick house"></div>
  <div class="photo photo-split-rail" role="img" aria-label="Photo of a split-rail fence with wire mesh and an arched wood gate"></div>

  <footer class="footer">
    <div class="contact-row" style="left:54px; top:26px;">
      <span class="social-dot"></span>
      <span style="margin-left:62px;">MeadowlarkRailGPV</span>
    </div>
    <div class="contact-row" style="left:54px; top:75px;">
      <svg class="contact-icon" viewBox="0 0 34 34"><circle cx="17" cy="17" r="16" fill="#3a83c9"/><path d="M11 9c1-1 2-1 3 0l2 3c.5 1 0 2-1 2.5-.5.5 0 2 2 4s3.5 2.5 4 2c.5-1 1.5-1.5 2.5-1l3 2c1 1 1 2 0 3-2 2-5 2-9-2s-4.5-7-2.5-9.5z" fill="#fff"/></svg>
      <span style="margin-left:14px;">704-555-0147</span>
    </div>
    <div class="contact-row" style="left:54px; top:114px;">
      <svg class="contact-icon" viewBox="0 0 34 34"><rect x="2" y="7" width="30" height="20" fill="#3a83c9"/><path d="M2 7l15 12 15-12M2 27l11-10M32 27l-11-10" stroke="#553d2b" stroke-width="2" fill="none"/></svg>
      <span style="margin-left:12px;">office@getbramblerail.com</span>
    </div>
    <div class="contact-row" style="left:54px; top:154px;">
      <svg class="contact-icon" viewBox="0 0 34 34" fill="none" stroke="#3a83c9" stroke-width="2"><circle cx="16" cy="16" r="13"/><ellipse cx="16" cy="16" rx="6" ry="13"/><path d="M3 16h26M5 9h22M5 23h22"/></svg>
      <span style="margin-left:14px;">http://getbramblerail.com</span>
    </div>
    <div class="contact-row" style="left:54px; top:196px; align-items:flex-start;">
      <svg class="contact-icon" viewBox="0 0 34 34"><path d="M17 5L3 17h4v12h8v-8h4v8h8V17h4z" fill="#3a83c9"/></svg>
      <span style="margin-left:13px; margin-top:-6px; line-height:21px;">436 Quillen rd, Monroe,<br>NC 28117</span>
    </div>

    <div class="divider-v"></div>
    <div class="hours">
      Office Hours:<br>
      Monday - Thursday: 9AM -11:30AM / 12:30PM - 3PM<br>
      Friday - 9AM - 1PM<br>
      Other Times By Appointment Only<br>
      Outdoor Showroom is Open 24/7<br>
      On Site Estimates Are Available By Appointment<br>
      Monday - Friday: 9AM - 5PM<br>
      Saturday: 9AM - 1PM
    </div>
    <div class="divider-h"></div>
    <p class="showroom">Come visit our outdoor showroom, open 24/7!</p>
  </footer>
</div>
</body>
</html>
```